Business Name "Open Meadow", Let your body do the talking through muscle testing. Tired of telli

There are 2 of us. We want the same basic card but different names and contact details. I will do my named one first and will confer with my business partner for this. I gather we then can get others printed with her name on it in the future. First things first.
Statement is "providing body/mind healing alternatives".
Lindenfold Method is the modality. This is an energy healing technique, which uses muscle testing. The progammes treat the body/mind as a computer. The practitioner establishes the current need of the body with the muslce test which is at the wrist, and relays the correction by first defraging and deleting stuck patterns, blockages and imbalances. Replacing that which is no longer required or that which is causing discomfort within the body/mind, with positive affirmation, energy flow and balance. Specific programmes are used for the specific needs. The programmes incorporate the meridians, chakras - the energies of the body - and emotions. Also provides vibrational infusions of vitamins, mineral, cell salts, bach flowers etc where the body has indicated there is imbalance. The body asks for what it needs for optimal function. It is client driven, the practitioner is just the vessel/pathway for relaying or facilitating the changes required.
I need a logo, and format. Card to be clear, bold, not 'fluffy'. Any colour that indicates healing and wellbeing.
I want the business name and statement to be in English and Maori.
To have my name and mobile number.
At this stage we do not have a permanent clinic address and will get a website in the future.
The card to indicate open to all people not just for those seeking the 'lightworkers' way.

Target Market(s)

Anybody who is willing can receive this therapy. Even babies in utero, surrogates and distant healing.

Industry/Entity Type

Clinic

Font styles to use
Sans Serif

Colors
f0edf5
6b449b
9bcb3c

Requirements
Must have
• Logo (I do not have one or any idea)
The following words to be written on it
'Open Meadow'
'providing body/mind healing alternatives'
'Lindenfold Method'
My name
and my contact details
'Open Meadow' and 'providing body/mind healing alternatives' to be written in italics or smaller print in MAORI

Nice to have
• Simple bold logo that has an eye catch appeal
Could use the name of business incorporated in the logo
White background is best
Clear crisp colours - 2 or 3 main colours
Should not have
• Black background
Too cramped
Too much detail

```html
<!DOCTYPE html>
<html lang="en">
<head>
<meta charset="utf-8">
<title>Open Meadow – Business Card</title>
<link rel="stylesheet" href="https://fonts.googleapis.com/css2?family=Open+Sans:ital,wght@0,300;0,400;1,300&display=swap">
<style>
  :root {
    --paper: #ffffff;
    --mist: #f0edf5;
    --violet: #6b449b;
    --violet-deep: #4f2f78;
    --leaf: #9bcb3c;
    --teal-mid: #1a8c9c;
    --teal-bright: #1597ad;
  }
  * { margin: 0; padding: 0; box-sizing: border-box; }
  html, body {
    width: 740px;
    height: 1200px;
    overflow: hidden;
    background: var(--paper);
  }
  .card {
    position: relative;
    width: 740px;
    height: 1200px;
    background: var(--paper);
    font-family: "Open Sans", sans-serif;
    line-height: 1;
  }
  .card > * { position: absolute; white-space: nowrap; }

  .brand-dot {
    left: 54px;
    top: 288px;
    width: 110px;
    height: 110px;
    border-radius: 50%;
    background: var(--leaf);
  }
  .brand-name {
    left: 189px;
    font-size: 105px;
    font-weight: 300;
    color: var(--violet);
  }
  .brand-name--first { top: 251px; }
  .brand-name--second { top: 355px; }

  .tagline {
    left: 0;
    width: 740px;
    text-align: center;
    font-size: 40px;
    font-style: italic;
    font-weight: 300;
    letter-spacing: 1px;
    color: var(--teal-mid);
  }
  .tagline--first { top: 516px; }
  .tagline--second { top: 566px; }

  .modality {
    left: 0;
    width: 740px;
    top: 650px;
    text-align: center;
    font-size: 43px;
    font-weight: 300;
    letter-spacing: 9px;
    text-transform: uppercase;
    color: var(--violet-deep);
  }

  .maori {
    left: 0;
    width: 740px;
    text-align: center;
    font-size: 26px;
    font-style: italic;
    font-weight: 300;
    letter-spacing: 1px;
    color: var(--violet);
  }
  .maori--name { top: 752px; }
  .maori--statement { top: 792px; }

  .person {
    left: 0;
    width: 740px;
    text-align: center;
    font-size: 66px;
    color: var(--teal-bright);
    text-transform: uppercase;
  }
  .person--given { top: 896px; font-weight: 300; letter-spacing: 2px; }
  .person--family { top: 982px; font-weight: 400; }

  .contact {
    left: 0;
    width: 740px;
    top: 1068px;
    text-align: center;
    font-size: 43px;
    font-weight: 300;
    letter-spacing: 1px;
    color: var(--teal-bright);
  }
</style>
</head>
<body>
  <main class="card">
    <span class="brand-dot" aria-hidden="true"></span>
    <h1 class="brand-name brand-name--first">Open</h1>
    <span class="brand-name brand-name--second">Meadow</span>

    <p class="tagline tagline--first">Providing Body/</p>
    <p class="tagline tagline--second">Mind Healing Alternatives</p>

    <p class="modality">Lindenfold Method</p>

    <p class="maori maori--name" lang="mi">Mānia Tuwhera</p>
    <p class="maori maori--statement" lang="mi">He huarahi rongoā mō te tinana me te hinengaro</p>

    <p class="person person--given">Clara</p>
    <p class="person person--family">Hensley</p>
    <p class="contact">Mobile: 027 4150628</p>
  </main>
</body>
</html>
```